Logo and business card

RVK Financial Solutions - Branding & Image Project

There will be 3 companies in our group. We want a similar Branding look & feel for all 3. The first company is DLW Financial which is already established, and I have included samples of the branding.

The goal for this design project is to create the corporate branding for RVK Financial Solutions which is the second company in the group.

Please use the same colours and fonts that we use at DLW Financial but the logo must be different. The final design should communicate financial safety and growth. Our typical clients are 40+ years and financially conservative.

Can you create a sample version using the dark green in the attached image.

We will need print resolution files and low res file for email, web etc.

The main printed outputs we need are – see separate attachment for examples;
Business Card 2 sided
Web logo

We’ll then need the following
Letterhead & follow on sheets
Envelopes C5 2 sided & C4 2 sided
Compliment Slips

```html
<!DOCTYPE html>
<html lang="en">
<head>
<meta charset="utf-8">
<title>RVK Financial Solutions – Business Card</title>
<link rel="stylesheet" href="https://fonts.googleapis.com/css2?family=Carlito:wght@400;700&display=swap">
<style>
  :root {
    --page-bg: #e8e6e3;
    --gold: #bf8a3e;
    --charcoal: #2b2b2b;
    --ink: #1c1c1c;
    --card-text: #fdf6ea;
    --frost-light: #f4f2f2;
    --frost-mid: #d9d4d4;
    --frost-dark: #a9a3a4;
  }
  * { margin: 0; padding: 0; box-sizing: border-box; }
  html, body {
    width: 1200px;
    height: 900px;
    overflow: hidden;
    background: var(--page-bg);
    font-family: "Carlito", "Calibri", sans-serif;
  }
  .business-card {
    position: absolute;
    left: 100px;
    top: 140px;
    width: 1000px;
    height: 619px;
    background: var(--gold);
    overflow: hidden;
    box-shadow: 0 10px 30px rgba(0,0,0,0.18);
  }
  .card-side-band {
    position: absolute;
    left: 717px;
    top: 0;
    width: 283px;
    height: 100%;
    background: var(--charcoal);
  }
  .brand-disc {
    position: absolute;
    left: 461px;
    top: 59px;
    width: 498px;
    height: 498px;
    border-radius: 50%;
    background: radial-gradient(circle at 40% 35%, var(--frost-light) 0%, var(--frost-mid) 55%, var(--frost-dark) 100%);
  }
  .brand-lockup {
    position: absolute;
    left: 0;
    top: 222px;
    width: 100%;
    display: flex;
    justify-content: center;
    align-items: center;
    gap: 14px;
  }
  .brand-mark {
    width: 26px;
    height: 26px;
    border-radius: 50%;
    background: var(--gold);
    flex: none;
  }
  .brand-name {
    font-size: 40px;
    font-weight: 400;
    color: var(--ink);
    white-space: nowrap;
    line-height: 1;
  }
  .adviser-name {
    position: absolute;
    left: 46px;
    top: 62px;
    font-size: 46px;
    font-weight: 700;
    color: var(--card-text);
    line-height: 1;
  }
  .adviser-role {
    position: absolute;
    left: 46px;
    top: 111px;
    font-size: 27px;
    font-weight: 400;
    color: var(--card-text);
    line-height: 1;
  }
  .office-address {
    position: absolute;
    left: 46px;
    top: 206px;
    font-size: 27px;
    line-height: 36.5px;
    color: var(--card-text);
    font-style: normal;
  }
  .contact-list {
    position: absolute;
    left: 46px;
    top: 414px;
    list-style: none;
    font-size: 27px;
    color: var(--card-text);
  }
  .contact-item {
    display: flex;
    align-items: center;
    height: 35.7px;
    white-space: nowrap;
  }
  .contact-icon {
    width: 28px;
    height: 28px;
    margin-right: 8px;
    flex: none;
  }
</style>
</head>
<body>
  <main class="business-card">
    <div class="card-side-band"></div>

    <div class="brand-disc" role="img" aria-label="Frosted silver disc carrying the company name">
      <div class="brand-lockup">
        <span class="brand-mark"></span>
        <span class="brand-name">RVK Financial Solutions</span>
      </div>
    </div>

    <h1 class="adviser-name">Morgan Halden</h1>
    <p class="adviser-role">Senior Wealth Adviser</p>

    <address class="office-address">
      The Old Granary, Unit 5<br>
      Millbrook Business Park<br>
      Ashwell Lane, Hinxworth<br>
      Baldock, Herts, sg7 4QX
    </address>

    <ul class="contact-list">
      <li class="contact-item">
        <svg class="contact-icon" viewBox="0 0 28 28" aria-hidden="true">
          <rect x="0" y="0" width="28" height="28" rx="4" fill="#fdf6ea"/>
          <path d="M8 6 L11 6 L12.5 10 L10.5 11.5 Q12 15.5 16.5 17.5 L18 15.5 L22 17 L22 20 Q21 22 18.5 22 Q7 20 6 9.5 Q6 7 8 6 Z" fill="#bf8a3e"/>
        </svg>
        01462 730415
      </li>
      <li class="contact-item">
        <svg class="contact-icon" viewBox="0 0 28 28" aria-hidden="true">
          <rect x="0" y="0" width="28" height="28" rx="4" fill="#fdf6ea"/>
          <rect x="8" y="4" width="12" height="20" rx="2" fill="#bf8a3e"/>
          <rect x="10" y="7" width="8" height="12" fill="#fdf6ea"/>
          <circle cx="14" cy="21.5" r="1.2" fill="#fdf6ea"/>
        </svg>
        07911 284637
      </li>
      <li class="contact-item">
        <svg class="contact-icon" viewBox="0 0 28 28" aria-hidden="true">
          <rect x="0" y="0" width="28" height="28" rx="4" fill="#fdf6ea"/>
          <rect x="4" y="7" width="20" height="14" fill="none" stroke="#bf8a3e" stroke-width="2"/>
          <path d="M4 7 L14 15 L24 7" fill="none" stroke="#bf8a3e" stroke-width="2"/>
        </svg>
        Morgan.halden@rvkfinancial.co.uk
      </li>
      <li class="contact-item">
        <svg class="contact-icon" viewBox="0 0 28 28" aria-hidden="true">
          <rect x="0" y="0" width="28" height="28" rx="4" fill="#fdf6ea"/>
          <circle cx="14" cy="14" r="9" fill="none" stroke="#bf8a3e" stroke-width="1.8"/>
          <ellipse cx="14" cy="14" rx="4" ry="9" fill="none" stroke="#bf8a3e" stroke-width="1.5"/>
          <line x1="5" y1="14" x2="23" y2="14" stroke="#bf8a3e" stroke-width="1.5"/>
          <line x1="6.5" y1="9.5" x2="21.5" y2="9.5" stroke="#bf8a3e" stroke-width="1.2"/>
          <line x1="6.5" y1="18.5" x2="21.5" y2="18.5" stroke="#bf8a3e" stroke-width="1.2"/>
        </svg>
        www.rvkfinancial.co.uk
      </li>
    </ul>
  </main>
</body>
</html>
```